Eye Doctor Needs Updated Business Card

We need a standard US business card designed for an optometrist's practice. Our practice name is Halvorn Vision Center and attached you'll find our logos. We are located in a smaller community, we are a trusted source for eye care and designer eyewear. We have 2 different version of our logos, so both versions are attached. Our slogan is "Close to Home, Clear Sight for Life". I'd like to see designs with one of our logos on the front with our contact info, and have the slogan on the back by itself. Final design should be professional looking, include the colors of our logo or colors that compliment the logo. We want it to look appropriate for a healthcare practice but also up-to-date, eye-catching, to have the normal contact info like address, phone #, email, but also possibly room for additional contact info such as facebook.
Updates

I just uploaded .eps files to use instead of the jpeg. Hope that helps!

So many great designs! We tending to like the darker blues that are used in our logo as the main blue color for the business cards. We also really like the use of a water-mark type appearance on either the front and/or back, or the embossed look as well looks nice. Thank you all for such great designs!

We're preferring the designs where white and the darker blue used in our logo are the primary colors on the front, but with a little green used as well. Again though, thanks for all the impressive designs so far!

Industry/Entity Type

Healthcare

```html
<!DOCTYPE html>
<html lang="en">
<head>
<meta charset="utf-8">
<title>Halvorn Vision Center – Business Card</title>
<link href="https://fonts.googleapis.com/css2?family=Marcellus&family=Tinos&display=swap" rel="stylesheet">
<style>
  :root {
    --green: #0aa551;
    --green-dark: #1f7a45;
    --green-deep: #2a5e3d;
    --blue-dark: #2f5f7e;
    --ink: #555a5e;
    --slogan-ink: #3f4448;
    --frame: #9a9a9a;
    --paper: #ffffff;
    --page: #ffffff;
  }
  * { margin: 0; padding: 0; box-sizing: border-box; }
  html, body { width: 1043px; height: 1200px; overflow: hidden; background: var(--page); }
  .sheet { position: relative; width: 1043px; height: 1200px; }

  .card { position: absolute; left: 110px; width: 820px; background: var(--paper); overflow: hidden; }
  .card-front { top: 70px; height: 507px; border: 1px solid var(--frame); }
  .card-back { top: 618px; height: 503px; border: 1px solid #333; }

  .tab { position: absolute; left: 114px; width: 593px; height: 46px; background: var(--green); }
  .tab-top { top: 4px; border-radius: 0 0 16px 16px; }
  .tab-bottom { bottom: 0; border-radius: 16px 16px 0 0; }

  .brand-name { font-family: "Tinos", serif; font-weight: 400; color: var(--blue-dark); line-height: 1.15; }

  .front-brand { position: absolute; left: 40px; top: 142px; width: 310px; text-align: center; }
  .brand-dot { display: block; margin: 0 auto 24px; width: 110px; height: 110px; border-radius: 50%; background: var(--blue-dark); }
  .front-brand .brand-name { font-size: 30px; }

  .divider { position: absolute; left: 404px; top: 142px; width: 4px; height: 224px; background: var(--green); }

  .contact { position: absolute; left: 448px; top: 182px; list-style: none; font-family: "Tinos", serif; font-size: 23px; color: var(--ink); }
  .contact li { display: flex; align-items: center; height: 30px; margin-bottom: 23px; }
  .contact svg { width: 26px; height: 26px; margin-right: 8px; flex: none; }

  .back-dot { position: absolute; left: 40px; top: 136px; width: 192px; height: 192px; border-radius: 50%; background: var(--blue-dark); }
  .back-name { position: absolute; left: 262px; top: 188px; width: 540px; text-align: center; font-size: 50px; }
  .slogan { position: absolute; left: 262px; top: 290px; width: 540px; text-align: center; font-family: "Marcellus", serif; font-size: 27px; color: var(--slogan-ink); }

  .wave { position: absolute; left: 0; bottom: 0; width: 820px; height: 140px; }
</style>
</head>
<body>
<div class="sheet">

  <section class="card card-front">
    <div class="tab tab-top"></div>

    <div class="front-brand">
      <span class="brand-dot"></span>
      <p class="brand-name">Halvorn Vision Center</p>
    </div>

    <div class="divider"></div>

    <ul class="contact">
      <li>
        <svg viewBox="0 0 26 26" aria-hidden="true"><circle cx="13" cy="13" r="11.5" fill="none" stroke="var(--green)" stroke-width="2"/><path d="M9 7.5l2.3 0 1 3-1.5 1.3a8 8 0 0 0 3.6 3.6l1.3-1.5 3 1v2.3c0 .8-.7 1.4-1.5 1.3A11 11 0 0 1 7.6 9c0-.8.6-1.5 1.4-1.5z" fill="var(--green)"/></svg>
        877-555-0142
      </li>
      <li>
        <svg viewBox="0 0 26 26" aria-hidden="true"><circle cx="13" cy="13" r="11.5" fill="none" stroke="var(--green)" stroke-width="2"/><rect x="7" y="9" width="12" height="8.5" fill="none" stroke="var(--green)" stroke-width="1.6"/><path d="M7 9l6 5 6-5" fill="none" stroke="var(--green)" stroke-width="1.6"/></svg>
        customercare@halvornvision.com
      </li>
      <li>
        <svg viewBox="0 0 26 26" aria-hidden="true"><circle cx="13" cy="13" r="11.5" fill="none" stroke="var(--green)" stroke-width="2"/><ellipse cx="13" cy="13" rx="4.5" ry="11.5" fill="none" stroke="var(--green)" stroke-width="1.5"/><path d="M1.5 13h23M3.5 7.5h19M3.5 18.5h19" stroke="var(--green)" stroke-width="1.5"/></svg>
        www.halvornvision.com
      </li>
    </ul>

    <div class="tab tab-bottom"></div>
  </section>

  <section class="card card-back">
    <span class="back-dot"></span>
    <p class="back-name brand-name">Halvorn Vision Center</p>
    <p class="slogan">Close to Home, Clear Sight for Life</p>

    <svg class="wave" viewBox="0 0 820 140" preserveAspectRatio="none" aria-hidden="true">
      <path d="M0 36 C160 70 300 110 460 70 C600 36 720 20 820 26 L820 140 L0 140 Z" fill="var(--green-deep)"/>
      <path d="M0 56 C170 88 320 120 470 86 C610 54 730 34 820 34 L820 140 L0 140 Z" fill="var(--green-dark)"/>
      <path d="M0 74 C180 104 330 128 480 100 C620 72 740 50 820 44 L820 140 L0 140 Z" fill="var(--green)"/>
    </svg>
  </section>

</div>
</body>
</html>
```